business stationery

have a gorgeous logo that needs to be incorporated on stationery. Was hoping to do something on letterhead that was a paper that looked like "bark" from a tree or something that resembled the "woods." Soft paper with some very basic natural elements. Same thing for business cards. Think American lakeside cabin. Organic. Natural. Calm and welcoming but clear to read and understand. Wanted to use alot of black.

Target Market(s)

buyers of Tobias Wrenfield home. Client that would have more than one home and in need of rare pieces and items to furnish an upmarket lakeside holiday cabin in the woods. Someone who treasures beautiful hand made items, organic foods and a real crackling fire but with money to burn in it!

Industry/Entity Type

Business

Requirements
Must have
• My logo
My business name
www.fernandcopper.example
Natural almost raw effect paper
My ABN: 62 307 514 928 (to be placed in small writing at the bottom of card/letterhead)
Nice to have
• The website will consist of a cabin door that you "open" with a creak sound effect and then you go "inside" to look at the various rooms to start shopping. Want to bring that element of texture and warmth into the stationary also.
Should not have
• Anything modern or hard to read items

```html
<!DOCTYPE html>
<html lang="en">
<head>
<meta charset="utf-8">
<title>Fern &amp; Copper — Letterhead</title>
<link rel="stylesheet" href="https://fonts.googleapis.com/css2?family=Arimo:wght@400&family=IM+Fell+English+SC&display=swap">
<style>
  :root {
    --paper: #ffffff;
    --bark-pale: #f9ddcc;
    --bark-light: #f5cdb6;
    --bark-mid: #efb490;
    --bark-warm: #eb9c6e;
    --bark-deep: #e48b5c;
    --rule: #5a0f12;
    --ink: #231c1a;
    --ink-soft: #3e302c;
  }
  html, body {
    margin: 0;
    padding: 0;
    overflow: hidden;
    background: var(--paper);
  }
  .letterhead {
    position: relative;
    width: 848px;
    height: 1200px;
    overflow: hidden;
    background: var(--paper);
    font-family: "Arimo", Arial, sans-serif;
    color: var(--ink);
  }
  .bark-band {
    position: absolute;
    left: 0;
    width: 848px;
  }
  .bark-band--header {
    top: 0;
    height: 200px;
    background:
      linear-gradient(180deg, rgba(255,255,255,0) 0%, rgba(255,240,230,0.35) 100%),
      linear-gradient(90deg, var(--bark-warm) 0%, var(--bark-mid) 12%, var(--bark-light) 30%, var(--bark-pale) 50%, var(--bark-light) 70%, var(--bark-mid) 88%, var(--bark-warm) 100%);
  }
  .bark-band--footer {
    top: 1147px;
    height: 53px;
    background: linear-gradient(90deg, var(--bark-mid) 0%, var(--bark-light) 30%, var(--bark-mid) 60%, var(--bark-warm) 85%, var(--bark-deep) 100%);
  }
  .rule {
    position: absolute;
    left: 0;
    width: 848px;
    height: 8px;
    background: var(--rule);
  }
  .rule--header { top: 199px; }
  .rule--footer { top: 1139px; }
  .brand__name {
    position: absolute;
    left: 0;
    top: 104px;
    width: 866px;
    margin: 0;
    text-align: center;
    font-family: "IM Fell English SC", Georgia, serif;
    font-weight: 400;
    font-size: 68px;
    line-height: 1;
    letter-spacing: 1px;
    color: var(--ink);
  }
  .brand__byline {
    position: absolute;
    right: 224px;
    top: 180px;
    margin: 0;
    font-family: "IM Fell English SC", Georgia, serif;
    font-size: 10px;
    letter-spacing: 0.3px;
    color: var(--ink);
  }
  .website {
    position: absolute;
    left: 17px;
    top: 176px;
    margin: 0;
    font-size: 16px;
    color: var(--ink-soft);
  }
  .abn {
    position: absolute;
    left: 17px;
    top: 1152px;
    margin: 0;
    font-size: 16px;
    color: var(--ink-soft);
  }
</style>
</head>
<body>
  <main class="letterhead">
    <div class="bark-band bark-band--header" role="img" aria-label="Warm peach tree bark texture"></div>
    <div class="rule rule--header"></div>

    <header class="brand">
      <p class="brand__name">Fern &amp; Copper</p>
      <p class="brand__byline">By Maren Holt</p>
    </header>

    <p class="website">www.fernandcopper.example</p>

    <div class="rule rule--footer"></div>
    <div class="bark-band bark-band--footer" role="img" aria-label="Warm peach tree bark texture"></div>
    <p class="abn">ABN: 62 307 514 928</p>
  </main>
</body>
</html>
```